Online Home Automation business needs business card design

New business starting up that sells home-automation products in Australia. Business card needs to look very polished and professional. The business name is "Vesk Automation".
Updates

Thank you all for the great designs, We are really impressed. We are in the process of deciding on a design but keep the designs coming in.

Industry/Entity Type

Business

```html
<!DOCTYPE html>
<html lang="en">
<head>
<meta charset="utf-8">
<title>Vesk Automation – Business Card</title>
<link rel="stylesheet" href="https://fonts.googleapis.com/css2?family=Open+Sans:wght@400;600&display=swap">
<style>
  :root {
    --stage: #3a3a3a;
    --card-black: #0c0c0c;
    --card-charcoal: #262626;
    --brand-red: #e3222a;
    --paper: #ffffff;
    --ink: #111111;
    --soft-white: #e9e9e9;
    --divider: #2e2e2e;
  }
  * { box-sizing: border-box; margin: 0; padding: 0; }
  html, body {
    width: 1200px;
    height: 750px;
    overflow: hidden;
  }
  body {
    background: var(--stage);
    font-family: "Open Sans", Arial, sans-serif;
    position: relative;
  }
  .card {
    position: absolute;
    top: 211px;
    width: 511px;
    height: 293px;
    border-radius: 20px;
    overflow: hidden;
  }
  /* Front */
  .card-front {
    left: 79px;
    background: radial-gradient(ellipse at 40% 35%, var(--card-charcoal) 0%, var(--card-black) 75%);
  }
  .front-mark {
    position: absolute;
    left: 72px;
    top: 61px;
    width: 168px;
    height: 168px;
    border-radius: 50%;
    background: var(--brand-red);
  }
  .front-divider {
    position: absolute;
    left: 276px;
    top: 92px;
    width: 1px;
    height: 110px;
    background: var(--divider);
  }
  .front-name {
    position: absolute;
    left: 290px;
    top: 112px;
    color: var(--paper);
    font-weight: 400;
    font-size: 29px;
    line-height: 31px;
  }
  /* Back */
  .card-back {
    left: 608px;
    background: var(--paper);
  }
  .back-top {
    position: absolute;
    left: 0; top: 0;
    width: 100%;
    height: 178px;
    background: radial-gradient(ellipse at 35% 0%, var(--card-charcoal) 0%, var(--card-black) 80%);
  }
  .person {
    position: absolute;
    left: 243px;
    top: 133px;
  }
  .person-name {
    color: var(--brand-red);
    font-size: 19px;
    line-height: 22px;
  }
  .person-role {
    color: var(--soft-white);
    font-size: 13px;
    line-height: 17px;
    margin-left: 2px;
  }
  .back-brand {
    position: absolute;
    left: 27px;
    top: 197px;
    display: flex;
    align-items: center;
    gap: 8px;
  }
  .back-mark {
    width: 66px;
    height: 66px;
    border-radius: 50%;
    background: var(--ink);
  }
  .back-name {
    color: var(--ink);
    font-weight: 400;
    font-size: 22px;
    line-height: 28px;
  }
  .contact {
    position: absolute;
    left: 238px;
    top: 206px;
    list-style: none;
  }
  .contact li {
    display: flex;
    align-items: center;
    gap: 12px;
    height: 17px;
    color: var(--ink);
    font-size: 15px;
  }
  .contact svg {
    width: 14px;
    height: 12px;
    fill: var(--brand-red);
    flex: none;
  }
</style>
</head>
<body>
  <section class="card card-front">
    <div class="front-mark"></div>
    <div class="front-divider"></div>
    <h1 class="front-name">Vesk<br>Automation</h1>
  </section>

  <section class="card card-back">
    <div class="back-top"></div>
    <div class="person">
      <p class="person-name">Mara Lindqvist</p>
      <p class="person-role">Manager</p>
    </div>
    <div class="back-brand">
      <div class="back-mark"></div>
      <p class="back-name">Vesk<br>Automation</p>
    </div>
    <ul class="contact">
      <li>
        <svg viewBox="0 0 14 12" aria-hidden="true"><path d="M1 4 C1 1 13 1 13 4 L13 5 L10 5 L10 3.5 L4 3.5 L4 5 L1 5 Z M3 6 L11 6 L12 11 L2 11 Z"/></svg>
        <span>+61 400 218 905</span>
      </li>
      <li>
        <svg viewBox="0 0 14 12" aria-hidden="true"><path d="M7 0.5 A5.5 5.5 0 1 0 7.01 0.5 Z M7 1.6 A4.4 4.4 0 1 1 6.99 1.6 Z" fill-rule="evenodd"/><path d="M2 5.5 H12 V6.5 H2 Z M6.5 1 H7.5 V11 H6.5 Z"/></svg>
        <span>www.veskautomation.com.au</span>
      </li>
      <li>
        <svg viewBox="0 0 14 12" aria-hidden="true"><path d="M1 2 H13 L7 6.5 Z M1 3.3 L7 7.8 L13 3.3 V10.5 H1 Z"/></svg>
        <span>info@veskautomation.com.au</span>
      </li>
    </ul>
  </section>
</body>
</html>
```